Personal letterhead and stationary

I am looking for someone to design letterhead and stationary set for my personal use. I want something simple and timeless with a little bit of color. I like photography, computers and writing.

```html
<!DOCTYPE html>
<html lang="en">
<head>
<meta charset="utf-8">
<title>Oliver James Hartley — Letterhead</title>
<link rel="stylesheet" href="https://fonts.googleapis.com/css2?family=Josefin+Slab:wght@300;400&display=swap">
<style>
  :root {
    --paper: #f0e1c9;
    --ink: #232120;
    --rule: #2b2826;
  }
  * { margin: 0; padding: 0; box-sizing: border-box; }
  html, body {
    width: 1200px;
    height: 848px;
    overflow: hidden;
    background: var(--paper);
  }
  .letterhead {
    position: relative;
    width: 1200px;
    height: 848px;
    background: var(--paper);
    color: var(--ink);
    font-family: "Josefin Slab", Georgia, serif;
  }
  .header-rule {
    position: absolute;
    top: 279px;
    height: 15px;
    border-top: 2px solid var(--rule);
    border-bottom: 2px solid var(--rule);
  }
  .header-rule--left { left: 48px; width: 448px; }
  .header-rule--right { left: 680px; width: 502px; }

  .owner-name {
    position: absolute;
    left: 57px;
    top: 229px;
    font-size: 35px;
    font-weight: 400;
    letter-spacing: -1px;
    line-height: 1;
    white-space: nowrap;
  }
  .contact {
    position: absolute;
    font-weight: 300;
    line-height: 1;
    white-space: nowrap;
  }
  .contact--email { left: 55px; top: 298px; font-size: 23px; letter-spacing: -0.3px; }
  .contact--address { right: 18px; top: 298px; font-size: 23px; }
  .contact--phone {
    right: 48px;
    top: 234px;
    font-size: 29px;
    display: flex;
    align-items: center;
    gap: 10px;
  }
  .phone-icon { width: 26px; height: 34px; }

  .brand-seal {
    position: absolute;
    left: 483px;
    top: 180px;
    width: 202px;
    height: 202px;
  }
  .brand-name {
    position: absolute;
    left: 483px;
    top: 272px;
    width: 202px;
    text-align: center;
    font-size: 14px;
    font-weight: 400;
    letter-spacing: 0.5px;
    line-height: 1;
    color: var(--paper);
    white-space: nowrap;
  }
</style>
</head>
<body>
  <main class="letterhead">
    <div class="header-rule header-rule--left"></div>
    <div class="header-rule header-rule--right"></div>

    <h1 class="owner-name">OLIVER JAMES HARTLEY</h1>
    <p class="contact contact--email">Oliver@mailbox.com.au</p>

    <svg class="brand-seal" viewBox="0 0 202 202" aria-hidden="true">
      <circle cx="101" cy="101" r="100" fill="var(--ink)"/>
    </svg>
    <p class="brand-name">OLIVER JAMES HARTLEY</p>

    <p class="contact contact--phone">
      <svg class="phone-icon" viewBox="0 0 26 34" aria-hidden="true">
        <path d="M9 2 L14 9 L10 13 C11 18 14 23 18 26 L22 23 L25 29 L20 33 C11 30 3 19 3 8 Z" fill="var(--ink)"/>
      </svg>
      <span>041255501938</span>
    </p>
    <p class="contact contact--address">14 kerr st ballarat vic 3350</p>
  </main>
</body>
</html>
```